Business Card Design

I want a non fussy clear design. I like Vintage, Retro writing for the main name as it will be a banner for the roof sign.
Company name, address and ph no. I would also like a unisex symbol small in the corner of the card. The colour of the card does not have to be blue. But I do want a bright clean clear card. A head sillohette small in the other corner possibly.

Industry/Entity Type

Business

Contact Information for Business Card

Kestra Hair Design
318 Marlowe Road, Pennick
Ph (09) 4162093

Requirements
Must have
• The back of the card must have appointment time, date dont worry about the location as its obviously on the front of the card

```html
<!DOCTYPE html>
<html lang="en">
<head>
<meta charset="utf-8">
<title>Kestra Hair Design – Business Card</title>
<link rel="stylesheet" href="https://fonts.googleapis.com/css2?family=Graduate&family=Oswald:wght@500&display=swap">
<style>
  :root {
    --card-red: #ff0000;
    --frame-white: #ffffff;
    --text-white: #ffffff;
    --emblem-yellow: #fdd835;
  }
  html, body {
    margin: 0;
    padding: 0;
    width: 1200px;
    height: 741px;
    overflow: hidden;
    background: var(--card-red);
  }
  .card {
    position: relative;
    width: 1200px;
    height: 741px;
    background: var(--card-red);
  }
  .card__frame {
    position: absolute;
    left: 24px;
    top: 39px;
    width: 1154px;
    height: 671px;
    background: var(--frame-white);
  }
  .card__panel {
    position: absolute;
    left: 72px;
    top: 80px;
    width: 1056px;
    height: 586px;
    background: var(--card-red);
  }
  .card__details {
    position: absolute;
    left: 110px;
    top: 238px;
    width: 720px;
    text-align: center;
    color: var(--text-white);
  }
  .card__name {
    margin: 0;
    font-family: "Graduate", serif;
    font-weight: 400;
    font-size: 54px;
    line-height: 1;
    letter-spacing: 1px;
    text-transform: uppercase;
    white-space: nowrap;
  }
  .card__address,
  .card__phone {
    margin: 0;
    font-family: "Oswald", sans-serif;
    font-weight: 500;
    font-size: 38px;
    line-height: 1;
    white-space: nowrap;
  }
  .card__address {
    margin-top: 40px;
  }
  .card__phone {
    margin-top: 42px;
  }
  .card__emblem {
    position: absolute;
    left: 792px;
    top: 202px;
  }
</style>
</head>
<body>
  <div class="card">
    <div class="card__frame"></div>
    <div class="card__panel"></div>

    <div class="card__details">
      <h1 class="card__name">Kestra Hair Design</h1>
      <p class="card__address">318 Marlowe Road, Pennick</p>
      <p class="card__phone">Phone :&nbsp; (09) 4162093</p>
    </div>

    <svg class="card__emblem" width="262" height="336" viewBox="0 0 262 336"
         role="img" aria-label="Emblem area: overlapping side-profile head silhouettes in black and red on a yellow oval">
      <ellipse cx="131" cy="168" rx="130" ry="167" fill="var(--emblem-yellow)"/>
    </svg>
  </div>
</body>
</html>
```